Business Cards for a company that provides webstore services to veterinarians

We need business cards designed for our main service PawCartHub. PawCartHub is a webstore that veterinarian clinics can use to that will allow their clients to purchase products for their pets. Our company is Brindlow Veterinary Solutions (BVS). Our mission statement is We love pets! We will do everything possible to facilitate along, healthy and happy relationship with their families.

Target Market(s)

Veterinarians

Industry/Entity Type

Veterinary

Contact Information for Business Card

I would like the design to incorporate the colours our our company. Cards should have room for employee name, title (only necessary in two instances), phone number, mobile number, email address and linkedin symbol and related profile name ie Marla Quinton. I would like the PawCartHub logo to appear on one side and BVS logo to appear on the other. I will need both an english and french version. I can provide the french translation. Please focus on english version and then we will translate

Colors

Designer to choose colors to be used in the design.

Requirements
Must have
• one side - PawCartHub logo with persons name, phone number, mobile number, email address
• second side - BVS logo
• colours should be consistent with our company. colours are as follows:
• Red
• RGB: 190 / 30 / 45
• CYMK: 14 / 100 / 90 /10
• Hex: #BE1E2D
• Gray
• RGB: 88 / 89 / 86
• CYMK: 3 / 2 / 0 /64
• Hex: #585956
Nice to have
• address of company - can be on either side address is 4817 Feldmoor Street Suite 305 Burlington ON K2R 6T4. Toll free number will vary depending on person
• Linkedin symbol and name of person
• on second side with BVS logo our company's mission statement
Should not have
• nothing comes to mind

```html
<!DOCTYPE html>
<html lang="en">
<head>
<meta charset="utf-8">
<title>PawCartHub Business Cards</title>
<link href="https://fonts.googleapis.com/css2?family=Montserrat:wght@400;500;600;700&display=swap" rel="stylesheet">
<style>
  :root {
    --brand-red: #be1e2d;
    --brand-gray: #585956;
    --ink: #333333;
    --rule: #8a8a8a;
    --paper: #ffffff;
    --backdrop: #ecebe8;
    --star-tint: #f2f2f2;
    --profile-blue: #2a8cc7;
  }
  * { margin: 0; padding: 0; box-sizing: border-box; }
  html, body {
    width: 1200px; height: 480px; overflow: hidden;
    background: var(--backdrop);
    font-family: "Montserrat", sans-serif;
  }
  .canvas { position: relative; width: 1200px; height: 480px; }
  .card {
    position: absolute; top: 94px;
    width: 474px; height: 270px;
    background: var(--paper);
    overflow: hidden;
  }
  .card--front { left: 86px; }
  .card--back { left: 635px; }

  /* front */
  .wordmark {
    position: absolute; left: 0; right: 0; top: 50px;
    display: flex; justify-content: center; align-items: center; gap: 10px;
  }
  .wordmark__dot {
    width: 18px; height: 18px; border-radius: 50%;
    background: var(--brand-red);
  }
  .wordmark__name {
    font-size: 42px; font-weight: 500; color: var(--brand-gray);
    letter-spacing: -0.5px; line-height: 1;
  }
  .address {
    position: absolute; left: 0; right: 0;
    text-align: center; font-size: 13px; color: var(--ink);
    white-space: nowrap;
  }
  .card--front .address { top: 128px; }
  .rule { position: absolute; height: 1px; background: var(--rule); }
  .card--front .rule { top: 153px; left: 72px; width: 340px; }
  .contact {
    position: absolute; left: 0; right: 0;
    text-align: center; font-size: 13px; color: var(--ink);
    white-space: nowrap;
  }
  .contact--phones { top: 162px; }
  .contact--web {
    top: 181px; display: flex; justify-content: center; align-items: center; gap: 14px;
  }
  .contact__url { font-weight: 700; }
  .contact__profile { display: flex; align-items: center; gap: 3px; font-size: 11.5px; }
  .contact__profile-dot {
    width: 14px; height: 14px; border-radius: 50%; background: var(--profile-blue);
  }
  .band { position: absolute; left: 0; bottom: 0; width: 474px; height: 70px; }
  .staff {
    position: absolute; left: 0; right: 0; bottom: 20px;
    text-align: center; color: var(--paper); font-size: 17px; font-weight: 500;
  }
  .staff__title { font-size: 15px; font-weight: 400; }

  /* back */
  .stars {
    position: absolute; right: 0; top: 40px; width: 120px; height: 200px;
    background: radial-gradient(circle at 60% 40%, var(--star-tint), transparent 70%);
  }
  .company-name {
    position: absolute; left: 0; right: 0; top: 100px;
    display: flex; justify-content: center; align-items: center; gap: 10px;
  }
  .company-name__dot {
    width: 14px; height: 14px; border-radius: 50%; background: var(--brand-red);
  }
  .company-name__text {
    font-size: 22px; font-weight: 500; color: var(--brand-gray); line-height: 1;
    white-space: nowrap;
  }
  .card--back .web {
    position: absolute; left: 0; right: 0; top: 204px;
    text-align: center; font-size: 13px; font-weight: 600; color: var(--brand-red);
  }
  .card--back .address { top: 226px; }
  .card--back .rule { top: 250px; left: 66px; width: 340px; }
</style>
</head>
<body>
<div class="canvas">

  <section class="card card--front">
    <div class="wordmark">
      <span class="wordmark__name">PawCartHub</span>
      <span class="wordmark__dot"></span>
    </div>
    <p class="address">4817 Feldmoor Street Suite 305, Burlington ON K2R 6T4</p>
    <div class="rule"></div>
    <p class="contact contact--phones">Tel: 000.000.0000, Mob: 012.345.6789</p>
    <div class="contact contact--web">
      <span class="contact__url">www.pawcarthub.com</span>
      <span class="contact__profile"><span class="contact__profile-dot"></span>/Person name</span>
    </div>
    <svg class="band" viewBox="0 0 474 70" preserveAspectRatio="none">
      <defs>
        <linearGradient id="swoosh" x1="0" y1="0" x2="1" y2="0">
          <stop offset="0" stop-color="#4c4f53"/>
          <stop offset="0.6" stop-color="#9ea1a4"/>
          <stop offset="1" stop-color="#ffffff"/>
        </linearGradient>
      </defs>
      <path d="M0 30 Q120 6 222 4 Q80 20 0 48 Z" fill="url(#swoosh)"/>
      <path d="M0 56 Q150 4 300 4 Q420 4 474 40 L474 70 L0 70 Z" fill="var(--brand-red)"/>
    </svg>
    <p class="staff">PERSONS NAME, <span class="staff__title">Manager</span></p>
  </section>

  <section class="card card--back">
    <div class="stars" role="img" aria-label="Faint scattered star pattern"></div>
    <div class="company-name">
      <span class="company-name__dot"></span>
      <span class="company-name__text">Brindlow Veterinary Solutions</span>
    </div>
    <p class="web">www.PawCartHub.com</p>
    <p class="address">4817 Feldmoor Street Suite 305, Burlington ON K2R 6T4</p>
    <div class="rule"></div>
  </section>

</div>
</body>
</html>
```